Disposable Mini Sauce Pot Design for Asian Chain Food Brands

We operate a Hainan Chicken Rice takeout brand under the name Spin4Rye, with our official website: www.Spin4Rye.com.
We offer four signature house sauces and are launching brand-new packaging for our sauce line. We require custom graphic designs exclusively for the sauce cup lids.
Product Material & Base Specs
The sauce cups are made of PP plastic, available in two translucent base options: Translucent White and Translucent Orange.
Four Sauce Varieties for Individual Lid Designs
1. Red Sauce – Fried Sweet Chili Sauce
2.Green Sauce – Scallion Oil Dressing
3.Sweet Soy Sauce
4.Sweet Red Sauce (Special for Fried Chicken)
Differentiate each sauce lid design through unique graphics, typography, or illustrative elements for easy customer identification.
The marking NET WT 2 OZ must be clearly printed on every lid.
**There is no need to print full descriptive text or the full name of the sauces on each lid; the design only needs to clearly differentiate the four sauce varieties.
**Please reference the original design style and brand color palette shown on our official website, and feel free to fully unleash your creativity.

```html
<!DOCTYPE html>
<html lang="en">
<head>
<meta charset="utf-8">
<title>Spin4Rye Signature House Sauces – Lid Labels</title>
<link rel="stylesheet" href="https://fonts.googleapis.com/css2?family=Oswald:wght@500;600;700&family=Roboto:wght@700&display=swap">
<style>
  :root {
    --canvas: #ffffff;
    --ink: #ffffff;
    --corner: #111111;
    --green: #84ff00;
    --green-deep: #5cb800;
    --sweet-red: #950000;
    --sweet-red-deep: #6b0000;
    --chili: #cc0000;
    --chili-deep: #8f0000;
    --soy: #c67a00;
    --soy-deep: #8e5400;
  }
  * { margin: 0; padding: 0; box-sizing: border-box; }
  html, body { width: 1200px; height: 1200px; overflow: hidden; background: var(--canvas); }
  .sheet { position: relative; width: 1200px; height: 1200px; }

  .lid {
    position: absolute;
    width: 340px; height: 384px;
    background: var(--lid);
    border-radius: 0 42px 42px 42px;
    color: var(--ink);
    overflow: hidden;
  }
  .lid--green     { left: 171px; top: 163px; --lid: var(--green);     --deep: var(--green-deep); }
  .lid--sweet-red { left: 671px; top: 163px; --lid: var(--sweet-red); --deep: var(--sweet-red-deep); }
  .lid--chili     { left: 171px; top: 666px; --lid: var(--chili);     --deep: var(--chili-deep); }
  .lid--soy       { left: 671px; top: 666px; --lid: var(--soy);       --deep: var(--soy-deep); }

  .lid__tab { position: absolute; left: 0; top: 0; width: 47px; height: 48px; background: var(--corner); }

  .lid__tracks {
    position: absolute; left: 60px; top: 25px; width: 220px; height: 350px;
    background: radial-gradient(ellipse at 50% 45%, var(--deep) 0%, transparent 70%);
    opacity: 0.3;
  }

  .lid__range {
    position: absolute; left: 32px; top: 58px; height: 162px;
    writing-mode: vertical-rl; transform: rotate(180deg);
    font-family: "Oswald", sans-serif; font-weight: 700;
    font-size: 22px; letter-spacing: 1.5px; line-height: 27px;
    text-align: center;
  }

  .lid__title {
    position: absolute; left: 68px; top: 36px;
    font-family: "Oswald", sans-serif; font-weight: 700;
    font-size: 100px; line-height: 92px; letter-spacing: -1px;
    white-space: nowrap;
  }

  .lid__name {
    position: absolute; left: 69px; top: 233px; height: 29px;
    padding: 0 20px 0 8px;
    background: var(--ink); color: var(--lid);
    font-family: "Oswald", sans-serif; font-weight: 600;
    font-size: 23px; line-height: 29px; white-space: nowrap;
    clip-path: polygon(0 0, 100% 0, calc(100% - 7px) 20%, 100% 40%, calc(100% - 7px) 60%, 100% 80%, calc(100% - 7px) 100%, 0 100%);
  }

  .lid__note {
    position: absolute; left: 69px; top: 274px;
    font-family: "Oswald", sans-serif; font-weight: 600;
    font-size: 15px; letter-spacing: 1px; white-space: nowrap;
  }

  .lid__weight {
    position: absolute; left: 121px; top: 327px;
    font-family: "Oswald", sans-serif; font-weight: 500;
    font-size: 21px; letter-spacing: 0.3px;
  }

  .lid__chick {
    position: absolute; left: 232px; top: 320px; width: 34px; height: 34px;
    background: var(--ink); border-radius: 50%;
  }

  .lid__web {
    position: absolute; left: 291px; top: 175px; height: 176px;
    writing-mode: vertical-rl; transform: rotate(180deg);
    font-family: "Roboto", sans-serif; font-weight: 700;
    font-size: 15px; line-height: 20px; text-align: center;
  }
</style>
</head>
<body>
<main class="sheet">

  <article class="lid lid--green">
    <div class="lid__tab"></div>
    <div class="lid__tracks" role="img" aria-label="Scattered chicken footprint pattern"></div>
    <p class="lid__range">HOUSE SAUCES</p>
    <h2 class="lid__title">signa-<br>ture</h2>
    <p class="lid__name">Green Sauce</p>
    <p class="lid__note">SCALLION OIL DRESSING</p>
    <p class="lid__weight">NET WT 2OZ</p>
    <div class="lid__chick" role="img" aria-label="Small chick icon"></div>
    <p class="lid__web">www.Spin4Rye.com</p>
  </article>

  <article class="lid lid--sweet-red">
    <div class="lid__tab"></div>
    <div class="lid__tracks" role="img" aria-label="Scattered chicken footprint pattern"></div>
    <p class="lid__range">HOUSE SAUCES</p>
    <h2 class="lid__title">signa-<br>ture</h2>
    <p class="lid__name">Sweet Red Sauce</p>
    <p class="lid__note">SPECIAL FOR FRIED CHICKEN</p>
    <p class="lid__weight">NET WT 2OZ</p>
    <div class="lid__chick" role="img" aria-label="Small chick icon"></div>
    <p class="lid__web">www.Spin4Rye.com</p>
  </article>

  <article class="lid lid--chili">
    <div class="lid__tab"></div>
    <div class="lid__tracks" role="img" aria-label="Scattered chicken footprint pattern"></div>
    <p class="lid__range">HOUSE SAUCES</p>
    <h2 class="lid__title">signa-<br>ture</h2>
    <p class="lid__name">Red Chili Sauce</p>
    <p class="lid__note">FRIED SWEET CHILI SAUCE</p>
    <p class="lid__weight">NET WT 2OZ</p>
    <div class="lid__chick" role="img" aria-label="Small chick icon"></div>
    <p class="lid__web">www.Spin4Rye.com</p>
  </article>

  <article class="lid lid--soy">
    <div class="lid__tab"></div>
    <div class="lid__tracks" role="img" aria-label="Scattered chicken footprint pattern"></div>
    <p class="lid__range">HOUSE SAUCES</p>
    <h2 class="lid__title">signa-<br>ture</h2>
    <p class="lid__name">Sweet Soy Sauce</p>
    <p class="lid__note">PERFECT BALANCE OF SAVORY</p>
    <p class="lid__weight">NET WT 2OZ</p>
    <div class="lid__chick" role="img" aria-label="Small chick icon"></div>
    <p class="lid__web">www.Spin4Rye.com</p>
  </article>

</main>
</body>
</html>
```